Construction Company business card and Logo.

We need a business card for a Building Company.
We build and constuction manage.
A simple logo is also required. Ive attached some samples that may assist.
Logo colours: Blue,sunburnt orange,lime/green and brown/grey.
The Font for the Brevanta logo ive been using is Georgia.
Maybe the A in Brevanta can be like my logo design..?
All other font either calibri or arial, something simple.
Simple/modern and neat is what i am looking for.
My card should look organised to convey what the company is about.

Target Market(s)

Developers, architects, proffesionals in general

Industry/Entity Type

Business

Contact Information for Business Card

Brevanta Constructions Pty Ltd
ACN: 381 607 925 Lic:716382D
Dermot Halvorsen
Managing Director
0438 215 706
dermot@brevanta.com.au
www.brevanta.com.au
Industrial.Commercial.Residential.Build Management

Requirements
Must have
• Ive attached some ideas for the logo. Its simple. If you come up with something else, please show me as im not 100% sure of what i want.
The front of the card should be white.
The back of the card should have the company name and logo with Blue background
Should not have
• the design should be simple.
No old style fonts or italics etc

```html
<!DOCTYPE html>
<html lang="en">
<head>
<meta charset="utf-8">
<title>Brevanta Constructions – Business Card</title>
<link rel="stylesheet" href="https://fonts.googleapis.com/css2?family=Oswald:wght@300;400;500;600&display=swap">
<style>
  :root {
    --brand-blue: #3439a0;
    --ink-blue: #2c2f9b;
    --steel-grey: #b9babd;
    --mid-grey: #a4a5a8;
    --pale-grey: #d4d5d7;
    --card-white: #ffffff;
    --backdrop: #ecebe8;
  }
  * { box-sizing: border-box; margin: 0; padding: 0; }
  html, body {
    width: 1200px; height: 849px; overflow: hidden;
    background: var(--backdrop);
    font-family: "Oswald", Arial, sans-serif;
  }
  .canvas {
    position: relative; width: 1200px; height: 849px;
    display: flex; align-items: center; justify-content: center; gap: 40px;
  }
  .card {
    position: relative; width: 550px; height: 336px;
    box-shadow: 0 2px 10px rgba(0,0,0,.12);
    overflow: hidden;
  }
  /* Front */
  .card-front { background: var(--card-white); }
  .wordmark {
    position: absolute; left: 36px; top: 30px;
    display: flex; align-items: center; gap: 14px;
  }
  .wordmark-square { width: 38px; height: 38px; background: var(--pale-grey); }
  .wordmark-text { color: var(--pale-grey); font-weight: 500; text-transform: uppercase; line-height: .9; }
  .wordmark-name { font-size: 44px; letter-spacing: 1px; }
  .wordmark-sub { font-size: 17px; letter-spacing: 1.5px; }
  .person { position: absolute; left: 36px; top: 118px; text-transform: uppercase; line-height: 1; }
  .person-name { color: var(--ink-blue); font-weight: 600; font-size: 31px; letter-spacing: .5px; }
  .person-role { color: var(--mid-grey); font-weight: 500; font-size: 17px; letter-spacing: 1px; margin-top: 3px; }
  .contacts { position: absolute; left: 36px; top: 190px; list-style: none; }
  .contacts li {
    display: flex; align-items: center; gap: 14px; height: 26px;
    color: var(--ink-blue); font-weight: 500; font-size: 16px; letter-spacing: .8px; text-transform: uppercase;
  }
  .contacts svg { width: 26px; height: 18px; flex: none; }
  .registration {
    position: absolute; left: 76px; top: 272px;
    color: var(--pale-grey); font-weight: 400; font-size: 13px; letter-spacing: 1px; line-height: 1.25;
    text-transform: uppercase;
  }
  .services {
    position: absolute; right: 18px; bottom: 12px;
    color: var(--pale-grey); font-weight: 400; font-size: 15px; letter-spacing: 3px; text-transform: uppercase;
    display: flex; gap: 16px;
  }
  /* Back */
  .card-back { background: var(--brand-blue); display: flex; align-items: center; justify-content: center; }
  .back-mark { display: flex; align-items: center; gap: 16px; }
  .back-mark .wordmark-square { width: 44px; height: 44px; background: var(--card-white); }
  .back-mark .wordmark-text { color: var(--card-white); }
  .back-mark .wordmark-name { font-size: 50px; }
  .back-mark .wordmark-sub { font-size: 19px; }
</style>
</head>
<body>
<main class="canvas">
  <section class="card card-front" aria-label="Business card front">
    <div class="wordmark">
      <span class="wordmark-square"></span>
      <div class="wordmark-text">
        <div class="wordmark-name">Brevanta</div>
        <div class="wordmark-sub">Constructions Pty Ltd</div>
      </div>
    </div>
    <div class="person">
      <div class="person-name">Dermot Halvorsen</div>
      <div class="person-role">Managing Director</div>
    </div>
    <ul class="contacts">
      <li>
        <svg viewBox="0 0 26 18" aria-hidden="true"><rect x="3" y="2" width="20" height="5" rx="2" fill="var(--pale-grey)"/><rect x="5" y="8" width="16" height="9" rx="1" fill="var(--pale-grey)"/></svg>
        0438 215 706
      </li>
      <li>
        <svg viewBox="0 0 26 18" aria-hidden="true"><rect x="2" y="2" width="22" height="14" fill="var(--pale-grey)"/><path d="M2 2 L13 10 L24 2" fill="none" stroke="#fff" stroke-width="1.5"/></svg>
        dermot@brevanta.com.au
      </li>
      <li>
        <svg viewBox="0 0 26 18" aria-hidden="true"><circle cx="13" cy="9" r="8" fill="var(--pale-grey)"/><path d="M5 9 H21 M13 1 V17 M13 1 C8 5 8 13 13 17 M13 1 C18 5 18 13 13 17" fill="none" stroke="#fff" stroke-width="1"/></svg>
        www.brevanta.com.au
      </li>
    </ul>
    <div class="registration">
      <div>ACN: 381 607 925</div>
      <div>LIC:&nbsp;&nbsp;716382D</div>
    </div>
    <div class="services">
      <span>Industrial</span><span>Commercial</span><span>Residential</span><span>Build Management</span>
    </div>
  </section>

  <section class="card card-back" aria-label="Business card back">
    <div class="back-mark">
      <span class="wordmark-square"></span>
      <div class="wordmark-text">
        <div class="wordmark-name">Brevanta</div>
        <div class="wordmark-sub">Constructions Pty Ltd</div>
      </div>
    </div>
  </section>
</main>
</body>
</html>
```